Marlowe Holdings LLC - Business Cards

Need the following information on the cards:

Name: Dean R Vossler
Title: Chief Executive Manager

Business address:
412 N Ridgeview Lane #118
Linden Falls, Oh 60412

Phone: (630) 555-0148 - Business
KPV FFL license number: 5-21-xxx-xx-xx-04519
Email: dean.vossler@marloweholdingsffl.com

Target Market(s)

Firearm owners

Industry/Entity Type

Firearms industry,

Contact Information for Business Card

Contact number, name and title, web page address, email, business address and kpv license number,

Requirements
Must have
• Name, title, business address, phone numbers, KPV license numbers, web page address and email address.
Nice to have
• Cellphone number,

```html
<!DOCTYPE html>
<html lang="en">
<head>
<meta charset="utf-8">
<title>Marlowe Holdings LLC – Business Cards</title>
<link rel="stylesheet" href="https://fonts.googleapis.com/css2?family=Montserrat:wght@400;500;600;700&display=swap">
<style>
  :root {
    --page: #e3e7e8;
    --ink: #1d1b1c;
    --card-black: #201d1e;
    --brand-red: #c3141c;
    --brand-red-dark: #7d0c11;
    --paper: #ffffff;
    --paper-shade: #e4e4e5;
    --rule: #3a3a3a;
    --white: #ffffff;
  }
  * { margin: 0; padding: 0; box-sizing: border-box; }
  html, body { width: 1200px; height: 800px; overflow: hidden; }
  body {
    background: var(--page);
    font-family: "Montserrat", sans-serif;
    color: var(--ink);
    position: relative;
  }

  .card {
    position: absolute;
    width: 432px;
    height: 270px;
    box-shadow: -2px 2px 4px rgba(0,0,0,0.18);
    overflow: hidden;
  }

  /* Front */
  .card-front {
    left: 193px;
    top: 102px;
    background: linear-gradient(180deg, var(--paper-shade) 0%, var(--paper) 58%, var(--paper) 100%);
    overflow: visible;
  }
  .front-band {
    position: absolute;
    left: 20px;
    top: 0;
    width: 181px;
    height: 270px;
    background: var(--card-black);
    overflow: hidden;
  }
  .band-mark {
    position: absolute;
    left: 0;
    right: 0;
    bottom: 22px;
    text-align: center;
    font-weight: 700;
    font-size: 13px;
    letter-spacing: 0.5px;
    color: rgba(255,255,255,0.09);
  }

  .ribbon {
    position: absolute;
    left: 13px;
    width: 195px;
    background: var(--brand-red);
    color: var(--white);
    font-size: 7.4px;
    font-weight: 500;
    line-height: 1.45;
    display: flex;
    align-items: center;
    padding-left: 17px;
  }
  .ribbon::before,
  .ribbon::after {
    content: "";
    position: absolute;
    bottom: -6px;
    width: 0; height: 0;
    border-top: 6px solid var(--brand-red-dark);
  }
  .ribbon::before { left: 0; border-left: 7px solid transparent; }
  .ribbon::after { right: 0; border-right: 7px solid transparent; }
  .ribbon-icon { width: 9px; height: 9px; margin-right: 8px; flex: none; fill: var(--white); }
  .ribbon-phone { top: 51px; height: 24px; }
  .ribbon-address { top: 98px; height: 35px; }
  .ribbon-email { top: 156px; height: 25px; }

  .brand-lockup {
    position: absolute;
    right: 12px;
    top: 20px;
    display: flex;
    align-items: center;
    gap: 4px;
  }
  .brand-dot {
    width: 14px; height: 14px;
    border-radius: 50%;
    background: var(--brand-red);
  }
  .brand-name {
    font-size: 8px;
    font-weight: 700;
    color: var(--brand-red);
    letter-spacing: 0.3px;
  }

  .holder-name {
    position: absolute;
    left: 223px;
    width: 198px;
    top: 102px;
    text-align: center;
    font-size: 24px;
    font-weight: 700;
    letter-spacing: 0.2px;
    padding-bottom: 3px;
    border-bottom: 1px solid var(--rule);
  }
  .holder-title {
    position: absolute;
    left: 223px;
    width: 198px;
    top: 138px;
    text-align: center;
    font-size: 8.6px;
    font-weight: 600;
  }
  .license {
    position: absolute;
    left: 223px;
    width: 198px;
    top: 245px;
    text-align: center;
    font-size: 6.8px;
    font-weight: 500;
  }

  /* Back */
  .card-back {
    left: 567px;
    top: 424px;
    width: 441px;
    height: 276px;
    background: var(--card-black);
    display: flex;
    flex-direction: column;
    align-items: center;
    justify-content: center;
    gap: 12px;
  }
  .back-circle {
    width: 80px; height: 80px;
    border-radius: 50%;
    border: 1.5px solid var(--white);
  }
  .back-name {
    font-size: 17px;
    font-weight: 600;
    letter-spacing: 1.5px;
    color: var(--white);
  }
</style>
</head>
<body>

  <section class="card card-front" aria-label="Business card front">
    <div class="front-band">
      <div class="band-mark">MARLOWE HOLDINGS LLC</div>
    </div>

    <div class="ribbon ribbon-phone">
      <svg class="ribbon-icon" viewBox="0 0 24 24" aria-hidden="true"><path d="M6.6 10.8a15.1 15.1 0 0 0 6.6 6.6l2.2-2.2a1 1 0 0 1 1-.25 11.4 11.4 0 0 0 3.6.57 1 1 0 0 1 1 1V20a1 1 0 0 1-1 1A17 17 0 0 1 3 4a1 1 0 0 1 1-1h3.5a1 1 0 0 1 1 1c0 1.25.2 2.45.57 3.57a1 1 0 0 1-.25 1z"/></svg>
      <span>(630) 555-0148</span>
    </div>

    <div class="ribbon ribbon-address">
      <svg class="ribbon-icon" viewBox="0 0 24 24" aria-hidden="true"><path d="M12 2a7 7 0 0 0-7 7c0 5.25 7 13 7 13s7-7.75 7-13a7 7 0 0 0-7-7zm0 9.5A2.5 2.5 0 1 1 12 6.5a2.5 2.5 0 0 1 0 5z"/></svg>
      <span>412 N Ridgeview Lane #118<br>Linden Falls, Oh 60412</span>
    </div>

    <div class="ribbon ribbon-email">
      <svg class="ribbon-icon" viewBox="0 0 24 24" aria-hidden="true"><path d="M2 5h20v14H2zm2 2v.5l8 5 8-5V7l-8 5z"/></svg>
      <span>dean.vossler@marloweholdingsffl.com</span>
    </div>

    <div class="brand-lockup">
      <span class="brand-dot"></span>
      <span class="brand-name">MARLOWE HOLDINGS LLC</span>
    </div>

    <h1 class="holder-name">Dean R Vossler</h1>
    <p class="holder-title">Chief Executive Manager</p>
    <p class="license">KPV FFL license number | 5-21-xxx-xx-xx-04519</p>
  </section>

  <section class="card card-back" aria-label="Business card back">
    <span class="back-circle"></span>
    <span class="back-name">MARLOWE HOLDINGS LLC</span>
  </section>

</body>
</html>
```